UI Design for a pre-ordering & Universal loyalty mobile app

We have built a central universal, preordering and gamification mobile app for alot of F&B merchant. The app is called PIXU (Pixoo as in eating something fast). Main goal for this app is too
1. Give users a universal loyalty system where they can accumulate loyalty points and use it on any brands
2. Gives user the ability to preorder for their food or drinks on the app and pick it up instore
3. There will be an E-wallet that is general or there can be a brand e-wallet (where they top-up with the brand only and get extra bonus)
4. There will be promotion such as games, top-up bonuses and rewards.
5. Community app where they can send money or promotion to their friends and will be able to play games together
This app is developed on the Flutter framework and also uses fontawesome font/icon package. Please consider this when doing the UI design for the app.
We are planning to create a mascot for our app as well and when it comes to color and icon, it's not set in stone and we are open for ideas.
I will attached our app icon and a few of our screens for your reference and each page details as follows:
Navigation bar.
There is a navigation bar on the top that should be visible on all screen. On the left will be a button to enter the menu which gives user more option and on the right will be a place for them to scan their QR code for loyalty points or payment and also a button to access their e-wallet.
1. Home screen
This screen is basically the main screen after user login. In this screen there will be
- Main banner (main promotions that's controlled by us)
- Specials banner (smaller) that will be controlled by the store/brands
- Favourite Store or Favourite food/drinks that user pre-configure
2. Shop screen (or can be called something else)
This screen is where they can browse all our participating stores. This screen will include
- Categories (filter)
- Brands which user can click and only view the brand page and stores
- All stores sorted by distances
3. Brand screen
The brand screen gives our brand with multiple store a presense on the app that is branded for them. They can have their own color scheme, logo and will only display their own store
4. Store screen
This will display all the store details, opening time, location, contact information etc.
- This screen will contain a banner/store image
- Store details
- Categories
- Food/drinks within the category
5. Order history screen
This will display their current order or their past order. Not sure if it should be on the main navigation or the sub navigation.
When making the UI design, please work on a color theme that will suit and also consider a mascot design in the future.
Feel free to ask me any questions before proceeding.
Thanks

```html
<!DOCTYPE html>
<html lang="en">
<head>
<meta charset="utf-8">
<title>Pixoo – Shop</title>
<link href="https://fonts.googleapis.com/css2?family=Outfit:wght@400;500;600&display=swap" rel="stylesheet">
<style>
:root{
  --bg:#f9f9fa;
  --ink:#1b1b1f;
  --muted:#9a9aa2;
  --chip:#f1f1f3;
  --green:#79c943;
  --green-dark:#3fae3a;
  --white:#ffffff;
  --line:#e2e2e6;
}
*{box-sizing:border-box;margin:0;padding:0}
html,body{width:1200px;height:2597px;overflow:hidden;background:var(--bg);font-family:"Outfit",sans-serif;color:var(--ink)}
.screen{position:relative;width:1200px;height:2597px}
.abs{position:absolute}
.status-time{left:74px;top:46px;font-size:44px;font-weight:600}
.status-icons{right:40px;top:48px}
.avatar{left:52px;top:196px;width:118px;height:124px;border-radius:50%;border:6px solid var(--green);background:linear-gradient(160deg,#6d8fa8,#cfd6da 60%,#8a9aa2)}
.greeting{left:212px;top:228px;font-size:52px;font-weight:600}
.round-btn{width:124px;height:124px;border-radius:50%;border:2px solid var(--line);display:flex;align-items:center;justify-content:center}
.scan-btn{left:824px;top:195px}
.wallet-btn{left:1006px;top:195px}
.dot{position:absolute;right:20px;top:22px;width:18px;height:18px;border-radius:50%;background:#f04a3e}
.search{left:50px;top:388px;width:898px;height:156px;border-radius:50px;background:var(--chip);display:flex;align-items:center;padding-left:50px;gap:40px;font-size:42px;color:var(--muted)}
.filter-btn{left:982px;top:388px;width:156px;height:156px;border-radius:40px;background:var(--white);box-shadow:0 24px 50px rgba(0,0,0,.05);display:flex;align-items:center;justify-content:center}
.section-title{font-size:50px;font-weight:600}
.chip{top:706px;height:96px;border-radius:26px;background:var(--chip);color:#9a9aa4;font-size:46px;display:flex;align-items:center;justify-content:center}
.brand{top:960px;width:134px;height:134px;border-radius:50%;display:flex;align-items:center;justify-content:center;font-size:26px;font-weight:600;color:var(--white)}
.see-all{right:66px;top:1180px;font-size:32px;font-weight:600;color:var(--green-dark)}
.store{left:50px;width:1094px;height:290px;border-radius:36px;background:var(--white);box-shadow:0 20px 40px rgba(0,0,0,.03);overflow:hidden}
.store-photo{position:absolute;left:0;top:0;width:338px;height:290px;border-radius:36px}
.fav{position:absolute;left:20px;top:20px;width:52px;height:52px;border-radius:50%;background:var(--green);display:flex;align-items:center;justify-content:center}
.rating{position:absolute;left:230px;top:20px;width:80px;height:36px;border-radius:18px;background:var(--white);font-size:17px;display:flex;align-items:center;justify-content:center;gap:6px;color:#555}
.store-body{position:absolute;left:374px;top:18px}
.store-name{font-size:40px;font-weight:500}
.tags{display:flex;gap:20px;margin-top:18px}
.tag{background:var(--chip);color:#8b8b93;font-size:19px;padding:6px 11px;border-radius:8px}
.addr{display:flex;align-items:center;gap:18px;font-size:31px;margin-top:18px}
.meta{display:flex;align-items:center;gap:16px;font-size:31px;color:var(--muted);margin-top:16px}
.meta .gap{width:28px}
.tabbar{left:0;top:2330px;width:1200px;height:267px;background:var(--white)}
.tab{position:absolute;top:60px;width:200px;display:flex;flex-direction:column;align-items:center;gap:22px;font-size:36px;color:#dcdce0}
.tab.active{color:var(--green)}
</style>
</head>
<body>
<div class="screen">
  <div class="abs status-time">9:41</div>
  <svg class="abs status-icons" width="196" height="36" viewBox="0 0 196 36">
    <rect x="0" y="22" width="8" height="10" rx="2" fill="#111"/><rect x="14" y="16" width="8" height="16" rx="2" fill="#111"/><rect x="28" y="9" width="8" height="23" rx="2" fill="#111"/><rect x="42" y="2" width="8" height="30" rx="2" fill="#111"/>
    <path d="M64 12a28 28 0 0 1 38 0M70 19a18 18 0 0 1 26 0M76 26a8 8 0 0 1 14 0" stroke="#111" stroke-width="5" fill="none" stroke-linecap="round"/>
    <rect x="124" y="4" width="62" height="28" rx="8" stroke="#999" stroke-width="2" fill="none"/><rect x="128" y="8" width="54" height="20" rx="5" fill="#111"/><rect x="189" y="13" width="4" height="10" rx="2" fill="#999"/>
  </svg>

  <div class="abs avatar" role="img" aria-label="User profile photo"></div>
  <div class="abs greeting">Hii, Rafiq</div>
  <div class="abs round-btn scan-btn">
    <svg width="68" height="56" viewBox="0 0 68 56" fill="none" stroke="#1b1b1f" stroke-width="5" stroke-linecap="round"><path d="M4 20V14A10 10 0 0 1 14 4h40a10 10 0 0 1 10 10v6M4 36v6a10 10 0 0 0 10 10h40a10 10 0 0 0 10-10v-6M2 28h64"/></svg>
  </div>
  <div class="abs round-btn wallet-btn">
    <svg width="70" height="62" viewBox="0 0 70 62" fill="none" stroke="#1b1b1f" stroke-width="5"><rect x="4" y="6" width="62" height="52" rx="14"/><path d="M66 24H52a8 8 0 0 0 0 16h14"/><circle cx="54" cy="32" r="2.5" fill="#1b1b1f"/></svg>
    <span class="dot"></span>
  </div>

  <div class="abs search">
    <svg width="50" height="50" viewBox="0 0 50 50" fill="none" stroke="#9a9aa2" stroke-width="4"><circle cx="22" cy="22" r="19"/><path d="M38 38l6 6" stroke-linecap="round"/></svg>
    Find for food or restaurant...
  </div>
  <div class="abs filter-btn">
    <svg width="64" height="60" viewBox="0 0 64 60"><path d="M4 14h56M4 46h56" stroke="#cfe9bd" stroke-width="5" stroke-linecap="round"/><circle cx="40" cy="14" r="11" fill="var(--green)"/><circle cx="24" cy="46" r="11" fill="var(--green)"/></svg>
  </div>

  <div class="abs section-title" style="left:50px;top:594px">Category</div>
  <div class="abs chip" style="left:50px;width:132px">Tea</div>
  <div class="abs chip" style="left:230px;width:304px">Bubble Tea</div>
  <div class="abs chip" style="left:584px;width:234px">Burger</div>
  <div class="abs chip" style="left:866px;width:234px">Coffee</div>
  <div class="abs chip" style="left:1148px;width:120px"></div>

  <div class="abs section-title" style="left:50px;top:854px">Brand</div>
  <div class="abs brand" style="left:50px;background:#5fb130">Brewly</div>
  <div class="abs brand" style="left:246px;background:#17679a">Ringo</div>
  <div class="abs brand" style="left:443px;background:#233476">Cupa</div>
  <div class="abs brand" style="left:640px;background:#1f7c52">Verde</div>
  <div class="abs brand" style="left:837px;background:#3b1c36">Plum</div>

  <div class="abs section-title" style="left:50px;top:1168px">Stories Near You</div>
  <div class="abs see-all">See All</div>

  <!-- store cards -->
  <div class="abs store" style="top:1300px">
    <div class="store-photo" role="img" aria-label="Cafe interior with tables and seated customers" style="background:linear-gradient(135deg,#3d3a38,#8b6a4c 55%,#4e5a5e)"></div>
    <div class="fav"><svg width="28" height="26" viewBox="0 0 28 26"><path d="M14 25S1 17 1 8a6.5 6.5 0 0 1 13-2 6.5 6.5 0 0 1 13 2c0 9-13 17-13 17z" fill="#fff"/></svg></div>
    <div class="rating"><span style="color:#f5b400">★</span>4.2</div>
    <div class="store-body">
      <div class="store-name">Demo 2 Perth</div>
      <div class="tags"><span class="tag">Tea</span><span class="tag">Bubble Tea</span><span class="tag">Buerger</span></div>
      <div class="addr"><svg width="28" height="34" viewBox="0 0 28 34"><path d="M14 33S1 20 1 13a13 13 0 0 1 26 0c0 7-13 20-13 20z" fill="var(--green)"/><circle cx="14" cy="13" r="5" fill="#fff"/></svg>123 A Street Somewhere Here</div>
      <div class="meta"><svg width="30" height="30" viewBox="0 0 30 30"><circle cx="15" cy="15" r="14" fill="var(--green)"/><path d="M15 7v9h6" stroke="#fff" stroke-width="3" fill="none"/></svg>15 min<span class="gap"></span><svg width="32" height="26" viewBox="0 0 32 26"><path d="M1 4l9-3 12 3 9-3v21l-9 3-12-3-9 3z" fill="var(--green)"/><path d="M10 1v21M22 4v21" stroke="#fff" stroke-width="2"/></svg>1.40 Km</div>
    </div>
  </div>

  <div class="abs store" style="top:1644px">
    <div class="store-photo" role="img" aria-label="Cafe dining room with wooden chairs and large windows" style="background:linear-gradient(135deg,#2e2622,#7a5238 55%,#b08660)"></div>
    <div class="fav"><svg width="28" height="26" viewBox="0 0 28 26"><path d="M14 25S1 17 1 8a6.5 6.5 0 0 1 13-2 6.5 6.5 0 0 1 13 2c0 9-13 17-13 17z" fill="#fff"/></svg></div>
    <div class="rating" style="left:236px"><span style="color:#f5b400">★</span>4.2</div>
    <div class="store-body" style="top:22px;left:376px">
      <div class="store-name">Brewly Mt Lawley</div>
      <div class="tags"><span class="tag">Tea</span><span class="tag">Bubble Tea</span><span class="tag">Buerger</span></div>
      <div class="addr"><svg width="28" height="34" viewBox="0 0 28 34"><path d="M14 33S1 20 1 13a13 13 0 0 1 26 0c0 7-13 20-13 20z" fill="var(--green)"/><circle cx="14" cy="13" r="5" fill="#fff"/></svg>Unit 12 Harbour St Northvale WA 6051</div>
      <div class="meta"><svg width="30" height="30" viewBox="0 0 30 30"><circle cx="15" cy="15" r="14" fill="var(--green)"/><path d="M15 7v9h6" stroke="#fff" stroke-width="3" fill="none"/></svg>15 min<span class="gap"></span><svg width="32" height="26" viewBox="0 0 32 26"><path d="M1 4l9-3 12 3 9-3v21l-9 3-12-3-9 3z" fill="var(--green)"/><path d="M10 1v21M22 4v21" stroke="#fff" stroke-width="2"/></svg>2.10 Km</div>
    </div>
  </div>

  <div class="abs store" style="top:1988px">
    <div class="store-photo" role="img" aria-label="Modern glass-fronted cafe building exterior" style="background:linear-gradient(135deg,#8d9296,#c9cdcf 50%,#4a4f52)"></div>
    <div class="fav"><svg width="28" height="26" viewBox="0 0 28 26"><path d="M14 25S1 17 1 8a6.5 6.5 0 0 1 13-2 6.5 6.5 0 0 1 13 2c0 9-13 17-13 17z" fill="#fff"/></svg></div>
    <div class="rating" style="left:236px"><span style="color:#f5b400">★</span>4.2</div>
    <div class="store-body">
      <div class="store-name">Leafhouse Broadway</div>
      <div class="tags"><span class="tag">Tea</span><span class="tag">Bubble Tea</span><span class="tag">Buerger</span></div>
      <div class="addr"><svg width="28" height="34" viewBox="0 0 28 34"><path d="M14 33S1 20 1 13a13 13 0 0 1 26 0c0 7-13 20-13 20z" fill="var(--green)"/><circle cx="14" cy="13" r="5" fill="#fff"/></svg>Unit 4 88 Meadow Rd Eastfield WA 6010</div>
      <div class="meta"><svg width="30" height="30" viewBox="0 0 30 30"><circle cx="15" cy="15" r="14" fill="var(--green)"/><path d="M15 7v9h6" stroke="#fff" stroke-width="3" fill="none"/></svg>15 min<span class="gap"></span><svg width="32" height="26" viewBox="0 0 32 26"><path d="M1 4l9-3 12 3 9-3v21l-9 3-12-3-9 3z" fill="var(--green)"/><path d="M10 1v21M22 4v21" stroke="#fff" stroke-width="2"/></svg>3.41 Km</div>
    </div>
  </div>

  <nav class="abs tabbar">
    <div class="tab" style="left:90px">
      <svg width="64" height="66" viewBox="0 0 64 66"><path d="M4 26L32 4l28 22v28a10 10 0 0 1-10 10H14A10 10 0 0 1 4 54z" fill="#dcdce0"/><path d="M24 50h16" stroke="#fff" stroke-width="4" stroke-linecap="round"/></svg>Home</div>
    <div class="tab active" style="left:382px">
      <svg width="70" height="66" viewBox="0 0 70 66"><path d="M2 4h8l4 8h52l-6 28a8 8 0 0 1-8 6H20a8 8 0 0 1-8-6z" fill="var(--green)"/><path d="M30 28h12" stroke="#fff" stroke-width="4" stroke-linecap="round"/><circle cx="20" cy="60" r="4" fill="var(--green)"/><circle cx="52" cy="60" r="4" fill="var(--green)"/></svg>Cart</div>
    <div class="tab" style="left:624px">
      <svg width="56" height="60" viewBox="0 0 56 60"><path d="M10 2h26l18 18v28a10 10 0 0 1-10 10H10A10 10 0 0 1 0 48V12A10 10 0 0 1 10 2z" fill="#dcdce0"/><path d="M14 30h16M14 40h22" stroke="#fff" stroke-width="4" stroke-linecap="round"/></svg>Orders</div>
    <div class="tab" style="left:906px">
      <svg width="52" height="66" viewBox="0 0 52 66"><circle cx="26" cy="16" r="15" fill="#dcdce0"/><path d="M0 56a26 14 0 0 1 52 0 10 10 0 0 1-10 10H10A10 10 0 0 1 0 56z" fill="#dcdce0"/></svg>Profile</div>
  </nav>
</div>
</body>
</html>
```